Business Cards/Stationary for CIO Outsourcing Company
Velmora Solutions
Use same font as used in my logo
Dorian Halbrook
Partner
Four Maple Ridge Plaza
Suite 240
Brookhaven, Texas 77590
dhalbrook@govelmora.com
www.govelmora.com
Logo icon can be shown separate from the name if necessary on stationary.

```html
<!DOCTYPE html>
<html lang="en">
<head>
<meta charset="utf-8">
<title>Velmora Solutions Stationery</title>
<link href="https://fonts.googleapis.com/css2?family=Libre+Baskerville&family=Open+Sans:wght@400;600&display=swap" rel="stylesheet">
<style>
:root{
  --bg:#8d8d8f;
  --paper:#ffffff;
  --red:#b31b22;
  --ink:#222222;
  --muted:#8a8a8a;
  --faint:#e6e3e1;
  --label:#f2f2f2;
}
*{box-sizing:border-box;margin:0;padding:0}
html,body{width:1200px;height:586px;overflow:hidden;background:var(--bg)}
.board{position:relative;width:1200px;height:586px;font-family:"Open Sans",Arial,sans-serif;color:var(--ink)}
.piece{position:absolute;background:var(--paper);box-shadow:0 2px 6px rgba(0,0,0,.35)}
.label{position:absolute;font-size:6px;color:var(--label);text-align:center;white-space:nowrap}
.brand{font-family:"Libre Baskerville",Georgia,serif;color:var(--ink);letter-spacing:1px;display:flex;align-items:center;gap:4px;white-space:nowrap}
.brand .dot{display:inline-block;border-radius:50%;background:var(--red)}
.brand-white{color:var(--paper)}
.brand-white .dot{background:var(--paper)}
.small{font-size:4px;line-height:5.5px;color:var(--ink)}
.folder{position:absolute;left:29px;top:53px;width:547px;height:504px}
.folder svg{display:block}
.card{width:101px;height:55px}
.letterhead{left:595px;top:180px;width:262px;height:377px}
.signature{left:864px;top:53px;width:312px;height:120px}
.env-front{left:864px;top:185px;width:312px;height:96px}
.env-back{width:312px;height:94px}
</style>
</head>
<body>
<main class="board">

  <div class="label" style="left:29px;top:42px;width:547px">Folder</div>
  <section class="folder">
    <svg width="547" height="504" viewBox="0 0 547 504">
      <rect x="0" y="0" width="270" height="504" fill="#fff"/>
      <rect x="277" y="0" width="270" height="504" fill="#fff"/>
      <path d="M0 405 H240 L270 504 H0Z" fill="#b31b22"/>
      <path d="M277 504 L307 405 H547 V504Z" fill="#b31b22"/>
      <circle cx="105" cy="190" r="80" fill="#ece9e7"/>
      <text x="105" y="290" text-anchor="middle" font-family="Libre Baskerville, serif" font-size="20" fill="#e2dedb" letter-spacing="2">VELMORA</text>
      <text x="105" y="388" text-anchor="middle" font-family="Open Sans, sans-serif" font-size="5" fill="#777">www.govelmora.com</text>
      <circle cx="110" cy="470" r="9" fill="#fff"/>
      <text x="110" y="452" text-anchor="middle" font-family="Open Sans, sans-serif" font-size="4" fill="#fff">www.govelmora.com</text>
      <circle cx="420" cy="470" r="9" fill="#fff"/>
      <text x="420" y="452" text-anchor="middle" font-family="Open Sans, sans-serif" font-size="4" fill="#fff">www.govelmora.com</text>
    </svg>
  </section>

  <div class="label" style="left:595px;top:21px;width:101px">Business Card Front</div>
  <article class="piece card" style="left:595px;top:29px">
    <div class="brand" style="position:absolute;left:8px;top:14px;font-size:7px"><span class="dot" style="width:6px;height:6px"></span>VELMORA</div>
    <div class="small" style="position:absolute;left:48px;top:26px">Dorian Halbrook<br>Partner<br>T 281.555.0142</div>
  </article>

  <div class="label" style="left:713px;top:21px;width:101px">Business Card Back - Option 1</div>
  <article class="piece card" style="left:713px;top:29px">
    <div class="small" style="position:absolute;left:8px;top:10px">Four Maple Ridge Plaza<br>Suite 240<br>Brookhaven, Texas 77590<br>dhalbrook@govelmora.com<br>www.govelmora.com</div>
  </article>

  <div class="label" style="left:595px;top:100px;width:101px">Business Card Back - Option 2</div>
  <article class="piece card" style="left:595px;top:108px">
    <div style="position:absolute;left:35px;top:12px;width:30px;height:30px;border-radius:50%;background:var(--faint)"></div>
    <div class="small" style="position:absolute;left:8px;top:44px;color:var(--muted)">www.govelmora.com</div>
  </article>

  <div class="label" style="left:713px;top:100px;width:101px">Business Card Back - Option 3</div>
  <article class="piece card" style="left:713px;top:108px;background:var(--red)">
    <div style="position:absolute;left:44px;top:20px;width:14px;height:14px;border-radius:50%;background:var(--paper)"></div>
  </article>

  <div class="label" style="left:595px;top:171px;width:262px">Letterhead</div>
  <article class="piece letterhead">
    <div class="brand" style="position:absolute;left:18px;top:22px;font-size:13px"><span class="dot" style="width:11px;height:11px"></span>VELMORA</div>
    <div class="small" style="position:absolute;left:186px;top:20px;font-size:3.5px;line-height:4.8px">Four Maple Ridge Plaza<br>Suite 240<br>Brookhaven, Texas 77590<br>T 281.555.0142<br>www.govelmora.com</div>
  </article>

  <div class="label" style="left:864px;top:43px;width:312px">E-mail Signature</div>
  <article class="piece signature">
    <div class="brand" style="position:absolute;left:18px;top:20px;font-size:9px"><span class="dot" style="width:8px;height:8px"></span>VELMORA</div>
    <div class="small" style="position:absolute;left:140px;top:16px;font-size:4.5px;line-height:6px">Dorian Halbrook<br>Partner<br>T 281.555.0142<br>dhalbrook@govelmora.com<br>www.govelmora.com</div>
  </article>

  <div class="label" style="left:864px;top:177px;width:312px">Envelope Front</div>
  <article class="piece env-front">
    <div class="brand" style="position:absolute;left:10px;top:10px;font-size:6px"><span class="dot" style="width:5px;height:5px"></span>VELMORA</div>
    <div class="small" style="position:absolute;left:10px;top:22px;font-size:3.5px;line-height:4.5px">Four Maple Ridge Plaza, Suite 240<br>Brookhaven, Texas 77590</div>
  </article>

  <article class="piece env-back" style="left:864px;top:293px">
    <svg width="312" height="94" viewBox="0 0 312 94"><path d="M0 0 L156 52 L312 0" fill="none" stroke="#ccc"/><path d="M0 94 L140 40 M312 94 L172 40" stroke="#e3e3e3" fill="none"/><circle cx="156" cy="40" r="5" fill="#b31b22"/></svg>
    <div class="label" style="left:0;top:58px;width:312px;color:var(--muted)">Envelope Back - Option 1</div>
  </article>
  <article class="piece env-back" style="left:864px;top:380px">
    <svg width="312" height="94" viewBox="0 0 312 94"><path d="M0 0 L156 52 L312 0" fill="none" stroke="#ccc"/><path d="M0 94 L140 40 M312 94 L172 40" stroke="#e3e3e3" fill="none"/><circle cx="156" cy="40" r="5" fill="#b31b22"/></svg>
    <div class="label" style="left:0;top:58px;width:312px;color:var(--muted)">Envelope Back - Option 2</div>
  </article>
  <article class="piece env-back" style="left:864px;top:464px">
    <svg width="312" height="94" viewBox="0 0 312 94"><path d="M0 0 L156 52 L312 0" fill="none" stroke="#ccc"/><path d="M0 94 L140 40 M312 94 L172 40" stroke="#e3e3e3" fill="none"/><circle cx="156" cy="40" r="5" fill="#b31b22"/></svg>
    <div class="label" style="left:0;top:58px;width:312px;color:var(--muted)">Envelope Back - Option 3</div>
  </article>

</main>
</body>
</html>
```